Group Medical Practice needs stationery, business cards etc. designed

We need stationery designed for a multisite practice that offers primary medical, dental and behavioral healthcare. We would like a design that is consistent for letterhead, business cards, Microsoft Outlook stationery etc. We have attached our new logo design.

Business

```html
<!DOCTYPE html>
<html lang="en">
<head>
<meta charset="utf-8">
<title>Cedar Ridge Health Services – Stationery</title>
<link href="https://fonts.googleapis.com/css2?family=Montserrat:wght@400;600&display=swap" rel="stylesheet">
<style>
  :root {
    --blue: #3763a8;
    --blue-dark: #2b4f8c;
    --green: #8cc63f;
    --paper: #ffffff;
    --paper-shade: #f3f4f6;
    --ink: #333840;
    --muted: #7a8089;
    --backdrop: #eceef1;
  }
  * { box-sizing: border-box; margin: 0; padding: 0; }
  html, body { width: 1200px; height: 907px; overflow: hidden; }
  body {
    background: var(--backdrop);
    font-family: "Montserrat", Arial, sans-serif;
    color: var(--ink);
    position: relative;
  }
  .item { position: absolute; box-shadow: 0 2px 6px rgba(0,0,0,.12); overflow: hidden; }
  .paper { background: var(--paper); }
  .blue-face { background: var(--blue); color: #fff; }

  .brand { display: flex; align-items: center; gap: 6px; font-weight: 600; letter-spacing: .04em; text-transform: uppercase; line-height: 1.1; }
  .brand-dot { width: 9px; height: 9px; border-radius: 50%; background: var(--green); flex: none; }
  .brand-name { color: var(--blue); }
  .blue-face .brand-name { color: #fff; }

  .swoosh { position: absolute; left: 0; bottom: 0; width: 100%; height: 44px; }

  /* Letterhead */
  .letterhead { left: 40px; top: 60px; width: 340px; height: 480px; padding: 34px 30px; }
  .letterhead .brand { font-size: 11px; }
  .letter-salutation { margin-top: 46px; font-size: 7.5px; font-weight: 600; }
  .letter-body { margin-top: 8px; font-size: 6.5px; line-height: 1.6; color: var(--muted); }
  .letter-body p + p { margin-top: 8px; }
  .letter-closing { margin-top: 14px; font-size: 6.5px; color: var(--muted); }
  .letter-signer { display: flex; align-items: flex-end; gap: 14px; margin-top: 4px; }
  .signer-name { font-size: 7.5px; font-weight: 600; color: var(--ink); }
  .signer-role { font-size: 6px; color: var(--muted); }
  .signature-area { width: 70px; height: 22px; background: linear-gradient(90deg, rgba(55,99,168,.25), rgba(55,99,168,.08)); border-radius: 3px; }
  .letter-footer { position: absolute; left: 30px; right: 30px; bottom: 52px; font-size: 5.5px; color: var(--muted); display: flex; gap: 10px; }

  /* Folder */
  .folder { left: 410px; top: 60px; width: 340px; height: 480px; display: flex; justify-content: center; padding-top: 70px; }
  .folder .brand { font-size: 14px; }

  /* Envelope */
  .envelope { left: 780px; top: 60px; width: 380px; height: 190px; }
  .envelope-flap { position: absolute; left: 0; top: 0; width: 100%; height: 54px; background: var(--blue); display: flex; justify-content: center; align-items: center; }
  .envelope-flap .brand-dot { width: 8px; height: 8px; }

  /* Compliment slip */
  .slip { left: 780px; top: 280px; width: 380px; height: 260px; padding: 40px 0 0; display: flex; flex-direction: column; align-items: center; }
  .slip .brand { font-size: 12px; }
  .slip-address { margin-top: 6px; font-size: 6px; color: var(--muted); }

  /* Business cards */
  .card { width: 300px; height: 170px; top: 580px; }
  .card-front { left: 40px; display: flex; justify-content: center; align-items: center; }
  .card-front .brand { font-size: 12px; }
  .card-back { left: 360px; padding-top: 34px; display: flex; flex-direction: column; align-items: center; }
  .card-back .brand { font-size: 10px; }
  .card-person { margin-top: 12px; font-size: 8px; font-weight: 600; color: var(--blue); }
  .card-role { font-size: 6px; color: var(--muted); margin-top: 2px; }
  .card-contact { margin-top: 8px; font-size: 5.5px; color: var(--muted); display: flex; gap: 8px; }

  /* Notebook */
  .notebook { left: 700px; top: 580px; width: 210px; height: 290px; display: flex; justify-content: center; padding-top: 60px; }
  .notebook .brand { font-size: 11px; }
  .notebook-spine { position: absolute; left: 0; top: 0; width: 14px; height: 100%; background: repeating-linear-gradient(180deg, var(--blue-dark) 0 6px, #555 6px 8px); }

  /* Key tag */
  .key-tag { left: 940px; top: 580px; width: 150px; height: 80px; display: flex; justify-content: center; align-items: center; border-radius: 6px; }
  .key-tag .brand { font-size: 9px; }
</style>
</head>
<body>

<svg width="0" height="0" style="position:absolute" aria-hidden="true">
  <defs>
    <symbol id="swoosh" viewBox="0 0 100 20" preserveAspectRatio="none">
      <path d="M0 17 C40 15 70 8 100 0 L100 3 C70 11 40 17 0 19 Z" fill="#8cc63f"/>
      <path d="M0 18.5 C30 18 60 14 85 8 C60 17 30 20 0 20 Z" fill="#3763a8"/>
    </symbol>
  </defs>
</svg>

<section class="item paper letterhead">
  <div class="brand"><span class="brand-dot"></span><span class="brand-name">Cedar Ridge<br>Health Services</span></div>
  <p class="letter-salutation">Dear sir / madame,</p>
  <div class="letter-body">
    <p>Thank you for choosing our practice for your family's care. Our teams in primary medicine, dentistry and behavioral health work together so every visit feels connected, clear and unhurried. Please review the enclosed details before your next appointment.</p>
    <p>If you have questions about scheduling, records or billing, our front desk is glad to help at any of our sites. We look forward to seeing you soon.</p>
  </div>
  <p class="letter-closing">Yours sincerely,</p>
  <div class="letter-signer">
    <div>
      <div class="signer-name">Lena Harrow</div>
      <div class="signer-role">Practice Director</div>
    </div>
    <div class="signature-area" role="img" aria-label="Handwritten signature"></div>
  </div>
  <div class="letter-footer">
    <span>Suite 3, 1420 Harbor Lane, Northfield 40210</span>
    <span>(555) 014-2290</span>
    <span>info@cedarridgehealth.example</span>
  </div>
  <svg class="swoosh"><use href="#swoosh"/></svg>
</section>

<section class="item blue-face folder">
  <div class="brand"><span class="brand-dot"></span><span class="brand-name">Cedar Ridge<br>Health Services</span></div>
</section>

<section class="item paper envelope">
  <div class="envelope-flap"><span class="brand-dot"></span></div>
</section>

<section class="item paper slip">
  <div class="brand"><span class="brand-dot"></span><span class="brand-name">Cedar Ridge<br>Health Services</span></div>
  <p class="slip-address">1420 Harbor Lane, Northfield</p>
  <svg class="swoosh"><use href="#swoosh"/></svg>
</section>

<section class="item blue-face card card-front">
  <div class="brand"><span class="brand-dot"></span><span class="brand-name">Cedar Ridge<br>Health Services</span></div>
</section>

<section class="item paper card card-back">
  <div class="brand"><span class="brand-dot"></span><span class="brand-name">Cedar Ridge<br>Health Services</span></div>
  <div class="card-person">Jordan Pell</div>
  <div class="card-role">Patient Coordinator</div>
  <div class="card-contact">
    <span>Suite 3, 1420 Harbor Lane, Northfield 40210</span>
    <span>(555) 014-2291</span>
    <span>info@cedarridgehealth.example</span>
  </div>
  <svg class="swoosh" style="height:30px"><use href="#swoosh"/></svg>
</section>

<section class="item blue-face notebook">
  <div class="notebook-spine"></div>
  <div class="brand"><span class="brand-dot"></span><span class="brand-name">Cedar Ridge<br>Health Services</span></div>
</section>

<section class="item paper key-tag">
  <div class="brand"><span class="brand-dot"></span><span class="brand-name">Cedar Ridge</span></div>
</section>

</body>
</html>
```